Family Farm Looking for meat label

We have a small farm in Italy with two types of cow "Piemontese" and "Pezzata Rossa Valdostana". We need label ( about 5x5 cm) to put on the boxes and on every single piece of meat.

Target Market(s)

private client

Industry/Entity Type

family farm

Colors

Designer to choose colors to be used in the design.

Requirements
Must have
• to write "Azienda Agricola Il Roveto" and the cow like our cow not differently. the Piemontese breed cow has the typical physical shapes as in the photo. No photo on the label just a drawing o something like that.
Nice to have
• just a one label, clear, fine and clean . Maybe with pastel color or watercolor. We are a small family farm.
Should not have
• no photo, no another type of cow

```html
<!DOCTYPE html>
<html lang="it">
<head>
<meta charset="utf-8">
<title>Etichette carne – Azienda Agricola Il Roveto</title>
<link rel="stylesheet" href="https://fonts.googleapis.com/css2?family=Bebas+Neue&family=Open+Sans:wght@700&display=swap">
<style>
  :root {
    --canvas: #f3eee6;
    --farm-green: #34b458;
    --salmon: #f37b6e;
    --cow-salmon: #f48c80;
    --cow-white: #fbfdfb;
    --white: #ffffff;
  }
  html, body {
    margin: 0;
    padding: 0;
    overflow: hidden;
  }
  .canvas {
    position: relative;
    width: 1200px;
    height: 884px;
    background: var(--canvas);
    overflow: hidden;
  }
  .meat-label {
    position: absolute;
    top: 215px;
    width: 417px;
    height: 404px;
    filter: drop-shadow(4px 5px 4px rgba(0,0,0,0.25));
  }
  .meat-label--piemontese { left: 144px; }
  .meat-label--valdostana { left: 625px; }
  .label-border { fill: var(--white); }
  .label-field { fill: var(--farm-green); }
  .breed-band { fill: var(--salmon); }
  .cow-area--piemontese { fill: var(--cow-salmon); }
  .cow-area--valdostana { fill: var(--cow-white); }
  .farm-mark {
    font-family: "Bebas Neue", sans-serif;
    font-size: 52px;
    fill: var(--white);
  }
  .breed-name {
    font-family: "Bebas Neue", sans-serif;
    fill: var(--white);
  }
  .farm-name {
    font-family: "Open Sans", sans-serif;
    font-weight: 700;
    font-size: 30px;
    letter-spacing: 1px;
    fill: var(--white);
  }
</style>
</head>
<body>
<main class="canvas">

  <svg class="meat-label meat-label--piemontese" viewBox="0 0 660 640" aria-label="Etichetta Piemontese">
    <path class="label-border" d="M16 130 H107 L320 0 L552 130 H641 Q657 130 657 146 V622 Q657 638 641 638 H16 Q0 638 0 622 V146 Q0 130 16 130 Z"/>
    <path class="label-field" d="M17 147 H125 L320 18 L535 147 H640 V620 H17 Z"/>
    <text class="farm-mark" x="320" y="155" text-anchor="middle">IL ROVETO</text>
    <rect class="cow-area--piemontese" role="img" aria-label="Sagoma di mucca Piemontese, bianca con mantello color salmone" x="127" y="205" width="340" height="225" rx="20"/>
    <rect class="breed-band" x="17" y="430" width="623" height="113"/>
    <text class="breed-name" x="324" y="515" text-anchor="middle" font-size="78">PIEMONTESE</text>
    <text class="farm-name" x="328" y="592" text-anchor="middle">Azienda Agricola Il Roveto</text>
  </svg>

  <svg class="meat-label meat-label--valdostana" viewBox="0 0 660 640" aria-label="Etichetta Pezzata Rossa Valdostana">
    <path class="label-border" d="M16 130 H107 L320 0 L552 130 H641 Q657 130 657 146 V622 Q657 638 641 638 H16 Q0 638 0 622 V146 Q0 130 16 130 Z"/>
    <path class="label-field" d="M17 147 H125 L320 18 L535 147 H640 V620 H17 Z"/>
    <text class="farm-mark" x="320" y="155" text-anchor="middle">IL ROVETO</text>
    <rect class="cow-area--valdostana" role="img" aria-label="Sagoma bianca di mucca Pezzata Rossa Valdostana" x="105" y="208" width="410" height="222" rx="20"/>
    <rect class="breed-band" x="17" y="430" width="623" height="113"/>
    <text class="breed-name" x="329" y="510" text-anchor="middle" font-size="62" textLength="538" lengthAdjust="spacingAndGlyphs">PEZZATA ROSSA VALDOSTANA</text>
    <text class="farm-name" x="337" y="590" text-anchor="middle">Azienda Agricola Il Roveto</text>
  </svg>

</main>
</body>
</html>
```